Stationary/business card for Custom Home builder
Pemberton Dwellings General Contractor
Simple
Travis Lindqvist
president
817 Calder Meadow Road
Dorrance Crossing, SC 29871
kbarlowbuilds@mailvero.net
Please use my logo

```html
<!DOCTYPE html>
<html lang="en">
<head>
<meta charset="utf-8">
<title>Pemberton Dwellings — Business Card</title>
<link href="https://fonts.googleapis.com/css2?family=EB+Garamond:ital,wght@0,400;0,500;0,600;1,400&display=swap" rel="stylesheet">
<style>
  :root{
    --bg:#e9e6e1;
    --brand-blue:#1f95d3;
    --brand-blue-light:#45b3e8;
    --brand-blue-dark:#1677ad;
    --paper:#ffffff;
    --ink:#4a4f55;
    --ink-soft:#7a8087;
    --shadow:rgba(40,30,20,.22);
  }
  *{box-sizing:border-box;margin:0;padding:0}
  html,body{width:1200px;height:629px;overflow:hidden}
  body{background:var(--bg);position:relative;font-family:"EB Garamond",Georgia,serif}

  .card{
    position:absolute;top:172px;width:500px;height:286px;border-radius:3px;
    box-shadow:0 10px 24px var(--shadow),0 2px 5px rgba(0,0,0,.1);
  }
  .card--front{left:70px;background:radial-gradient(ellipse at 50% 40%,var(--brand-blue-light),var(--brand-blue) 60%,var(--brand-blue-dark));color:#fff}
  .card--back{left:630px;background:var(--paper);color:var(--ink)}

  .brand{position:absolute;left:0;right:0;display:flex;align-items:center;justify-content:center;gap:14px}
  .brand__mark{width:34px;height:34px;flex:none;background:currentColor}
  .brand__name{font-family:"EB Garamond",Georgia,serif;font-weight:500;font-size:26px;line-height:1.1;text-align:left}
  .card--front .brand{top:112px;color:#fff}
  .card--back .brand{top:36px;color:var(--brand-blue)}

  .person{position:absolute;left:34px;top:170px}
  .person__name{font-weight:600;font-size:15px;letter-spacing:1px;color:var(--brand-blue)}
  .person__role{font-size:13px;font-style:italic;color:var(--ink-soft);margin-bottom:10px}
  .person__addr{font-size:13px;line-height:1.35}

  .contact{position:absolute;left:262px;top:166px;list-style:none}
  .contact li{display:flex;align-items:center;gap:8px;font-size:12.5px;line-height:1;margin-bottom:7px}
  .contact .icon{width:17px;height:17px;flex:none;border-radius:50%;background:var(--brand-blue);display:flex;align-items:center;justify-content:center}
  .contact svg{width:10px;height:10px;fill:none;stroke:#fff;stroke-width:1.6;stroke-linecap:round;stroke-linejoin:round}
</style>
</head>
<body>
  <section class="card card--front">
    <div class="brand">
      <span class="brand__mark" aria-hidden="true"></span>
      <p class="brand__name">Pemberton Dwellings<br>General Contractor</p>
    </div>
  </section>

  <section class="card card--back">
    <div class="brand">
      <span class="brand__mark" aria-hidden="true"></span>
      <p class="brand__name">Pemberton Dwellings<br>General Contractor</p>
    </div>

    <div class="person">
      <p class="person__name">TRAVIS LINDQVIST</p>
      <p class="person__role">President</p>
      <p class="person__addr">817 Calder Meadow Road<br>Dorrance Crossing, SC 29871</p>
    </div>

    <ul class="contact">
      <li><span class="icon"><svg viewBox="0 0 10 10"><path d="M2 1.2h1.8l.7 2-1 .8a5 5 0 0 0 2.5 2.5l.8-1 2 .7V8a1 1 0 0 1-1 1A7 7 0 0 1 1 2.2a1 1 0 0 1 1-1z"/></svg></span>(843) 555-0142</li>
      <li><span class="icon"><svg viewBox="0 0 10 10"><rect x="2" y="3" width="6" height="4"/><path d="M3 3V1h4v2M3 7v2h4V7"/></svg></span>(843) 555-0187</li>
      <li><span class="icon"><svg viewBox="0 0 10 10"><rect x="1" y="2.2" width="8" height="5.6"/><path d="M1 2.4l4 3 4-3"/></svg></span>kbarlowbuilds@mailvero.net</li>
      <li><span class="icon"><svg viewBox="0 0 10 10"><circle cx="5" cy="5" r="4"/><path d="M1 5h8M5 1c-2 2.4-2 5.6 0 8M5 1c2 2.4 2 5.6 0 8"/></svg></span>www.pembertondwellings.com</li>
    </ul>
  </section>
</body>
</html>
```